Corporate Two Sided Business Card

Looking for a Corporate "edgy" Modern look and feel for a business card

We are looking at two options. Dark background with our logo on it, white background with our logo on it - The background is more - Charcoal / Graphite then black

Details will be

Danielle Forsk

Licensee / Director

m. 0428 519 064

e. danielle@quorvela.com.au

quorvela.com.au

Target Market(s)

Professional Business people that refer use business and clients that own Investment Properties

Industry/Entity Type

Business

Contact Information for Business Card

Details will be

Danielle Forsk

Licensee / Director

m. 0428 519 064

quorvela.com.au

Font styles to use
Serif

Colors
000000
ec1f27
eeeeee
ffffff

Requirements
Must have
• Two options - White Background and Dark Background. - Two sided
Nice to have
• A design that is edgy, modern and new to look instead of boring style corporate cards - It should be a full integrated design
Should not have
• Block looking - Cheap.

```html
<!DOCTYPE html>
<html lang="en">
<head>
<meta charset="utf-8">
<title>Quorvela — Business Card</title>
<link href="https://fonts.googleapis.com/css2?family=Poppins:wght@400;500;600&display=swap" rel="stylesheet">
<style>
  :root {
    --stage: #e4e4e6;
    --charcoal: #1d1d20;
    --red: #ec1f27;
    --white: #ffffff;
    --ink: #4a4a4e;
    --rule-grey: #5a5a5e;
    --soft: #eeeeee;
  }
  * { box-sizing: border-box; margin: 0; padding: 0; }
  html, body { width: 1200px; height: 864px; overflow: hidden; }
  body {
    background: var(--stage);
    font-family: "Poppins", sans-serif;
    display: flex;
    align-items: center;
    justify-content: center;
    gap: 36px;
  }
  .card {
    position: relative;
    width: 540px;
    height: 330px;
    overflow: hidden;
    box-shadow: 0 10px 28px rgba(0,0,0,0.18);
  }

  /* Front — dark */
  .card--front { background: var(--charcoal); }
  .card--front .band-top {
    position: absolute; left: 0; right: 0; top: 0; height: 24px;
    background: var(--red);
  }
  .card--front .band-bottom {
    position: absolute; left: 0; right: 0; bottom: 0; height: 72px;
    background: var(--red);
    display: flex; align-items: center; justify-content: center;
  }
  .card--front .web {
    color: var(--white); font-size: 13px; font-weight: 500; letter-spacing: 0.4px;
  }
  .brand {
    display: flex; align-items: center; gap: 10px;
  }
  .brand-mark { width: 26px; height: 26px; background: var(--red); }
  .brand-name { font-weight: 600; line-height: 1; letter-spacing: 0.5px; }
  .card--front .brand {
    position: absolute; left: 0; right: 0; top: 98px; justify-content: center;
  }
  .card--front .brand-name { color: var(--white); font-size: 52px; }

  /* Back — white */
  .card--back { background: var(--white); }
  .card--back .brand {
    position: absolute; left: 40px; top: 130px;
  }
  .card--back .brand-mark { width: 20px; height: 20px; }
  .card--back .brand-name { color: var(--ink); font-size: 38px; }
  .divider {
    position: absolute; left: 292px; top: 86px; width: 1px; height: 124px;
    background: linear-gradient(to bottom, transparent, #9a9a9e 30%, #9a9a9e 70%, transparent);
  }
  .contact {
    position: absolute; left: 312px; top: 84px;
  }
  .contact .name { color: var(--ink); font-size: 21px; font-weight: 600; line-height: 1.1; }
  .contact .role { color: var(--red); font-size: 13px; font-weight: 400; margin-bottom: 10px; }
  .contact-list { list-style: none; }
  .contact-list li {
    display: flex; align-items: center; gap: 8px;
    color: var(--ink); font-size: 11.5px; margin-bottom: 6px;
  }
  .contact-icon {
    width: 18px; height: 18px; border-radius: 3px; background: var(--red);
    display: flex; align-items: center; justify-content: center; flex: none;
  }
  .rule {
    position: absolute; left: 0; right: 0; bottom: 26px; height: 5px; display: flex;
  }
  .rule .rule-red { flex: 0 0 62%; background: var(--red); }
  .rule .rule-grey { flex: 1; background: var(--rule-grey); }
</style>
</head>
<body>

  <section class="card card--front" aria-label="Card front">
    <div class="band-top"></div>
    <div class="brand">
      <span class="brand-mark"></span>
      <span class="brand-name">quorvela</span>
    </div>
    <div class="band-bottom">
      <span class="web">WWW.QUORVELA.COM.AU</span>
    </div>
  </section>

  <section class="card card--back" aria-label="Card back">
    <div class="brand">
      <span class="brand-mark"></span>
      <span class="brand-name">quorvela</span>
    </div>
    <div class="divider"></div>
    <div class="contact">
      <p class="name">Danielle Forsk</p>
      <p class="role">Licensee / Director</p>
      <ul class="contact-list">
        <li>
          <span class="contact-icon">
            <svg width="10" height="12" viewBox="0 0 10 12"><rect x="1.5" y="0.8" width="7" height="10.4" rx="1.2" fill="none" stroke="#fff" stroke-width="1.3"/><circle cx="5" cy="9.3" r="0.8" fill="#fff"/></svg>
          </span>
          0428 519 064
        </li>
        <li>
          <span class="contact-icon">
            <svg width="12" height="9" viewBox="0 0 12 9"><rect x="0.7" y="0.7" width="10.6" height="7.6" fill="none" stroke="#fff" stroke-width="1.2"/><path d="M0.7 0.9 L6 5 L11.3 0.9" fill="none" stroke="#fff" stroke-width="1.2"/></svg>
          </span>
          danielle@quorvela.com.au
        </li>
        <li>
          <span class="contact-icon">
            <svg width="12" height="12" viewBox="0 0 12 12"><circle cx="6" cy="6" r="5" fill="none" stroke="#fff" stroke-width="1.2"/><ellipse cx="6" cy="6" rx="2.2" ry="5" fill="none" stroke="#fff" stroke-width="1"/><path d="M1 6 H11" stroke="#fff" stroke-width="1"/></svg>
          </span>
          www.quorvela.com.au
        </li>
      </ul>
    </div>
    <div class="rule"><span class="rule-red"></span><span class="rule-grey"></span></div>
  </section>

</body>
</html>
```